Bright Current Electrical & Communications business card design

We would like a double sided business card that is different. Want it to be exciting and fun. Something that people keep rather then just throw it in the bin.
We have a logo that we want to put on one side of the business card and then the business information on the reverse side. Trying to go for a real professional style of business card

Target Market(s)

Electrical

Industry/Entity Type

Electrical

Contact Information for Business Card

Bright Current Electrical & Communications
Marcus Holloway
P: 0437 862 305
E: brightcurrent@mailbox-example.com.au
Lic No: 574106K
24/7

Font styles to use
Other font styles liked:
• Would like ideas

Requirements
Must have
• Our company logo (preferably on both sides) yellow needs to be incorporated somewhere. Business card card colours to match with logo. Maybe a small pop of colour
Nice to have
• Open to some design ideas

```html
<!DOCTYPE html>
<html lang="en">
<head>
<meta charset="utf-8">
<title>Bright Current Electrical &amp; Communications – Business Card</title>
<link rel="stylesheet" href="https://fonts.googleapis.com/css2?family=Exo+2:wght@700&family=Roboto:wght@300;400;700&display=swap">
<style>
  :root {
    --page-bg: #e9e7e3;
    --card-white: #fbfbfb;
    --card-white-edge: #ececec;
    --ink-dark: #2b2b2b;
    --ink-mid: #4a4a4a;
    --ink-light: #9c9c9c;
    --accent-yellow: #f2df1f;
    --swoosh-grey: #d9d9d9;
    --back-grey-light: #8f8f8f;
    --back-grey-dark: #5e5e5e;
    --back-ink: #f4f4f4;
  }
  * { box-sizing: border-box; margin: 0; padding: 0; }
  html, body { width: 1200px; height: 780px; overflow: hidden; }
  body {
    background: var(--page-bg);
    display: flex;
    align-items: center;
    justify-content: center;
    gap: 40px;
    font-family: "Roboto", Arial, sans-serif;
  }
  .card {
    width: 540px;
    height: 309px;
    position: relative;
    overflow: hidden;
    box-shadow: 0 6px 18px rgba(0,0,0,0.18);
  }

  /* Front: contact side */
  .card--front {
    background: linear-gradient(160deg, var(--card-white) 55%, var(--card-white-edge));
  }
  .front-swoosh { position: absolute; left: 0; bottom: 0; width: 540px; height: 309px; }
  .brand {
    position: absolute;
    left: 30px;
    top: 44px;
    width: 250px;
  }
  .brand-mark {
    display: flex;
    align-items: center;
    gap: 10px;
  }
  .brand-square {
    width: 18px; height: 18px;
    background: var(--accent-yellow);
    flex: none;
  }
  .brand-name {
    font-family: "Exo 2", Arial, sans-serif;
    font-weight: 700;
    color: var(--ink-dark);
    font-size: 17px;
    line-height: 1.15;
    text-transform: uppercase;
    letter-spacing: 0.5px;
  }
  .brand-rule {
    margin-top: 10px;
    height: 1.5px;
    width: 230px;
    background: var(--accent-yellow);
  }
  .contact {
    position: absolute;
    right: 30px;
    top: 46px;
    text-align: right;
  }
  .contact-name {
    font-weight: 300;
    font-size: 27px;
    color: var(--ink-light);
    letter-spacing: 0.5px;
    margin-bottom: 16px;
  }
  .contact-line {
    display: flex;
    justify-content: flex-end;
    align-items: center;
    gap: 7px;
    font-size: 13px;
    color: var(--ink-mid);
    margin-bottom: 6px;
  }
  .contact-line--phone { font-size: 16px; }
  .contact-icon {
    width: 14px; height: 14px;
    background: var(--accent-yellow);
    display: inline-flex;
    align-items: center;
    justify-content: center;
    flex: none;
  }
  .contact-licence {
    font-weight: 700;
    font-size: 15px;
    color: var(--ink-dark);
    margin-top: 4px;
  }
  .cable-photo {
    position: absolute;
    left: 190px;
    top: 170px;
    width: 140px;
    height: 120px;
    border-radius: 6px 6px 40px 40px;
    background: radial-gradient(ellipse at 50% 30%, #f3f3f3, #c9c9c9 70%, #b5b5b5);
  }

  /* Back: brand side */
  .card--back {
    background: radial-gradient(ellipse at 40% 35%, var(--back-grey-light), var(--back-grey-dark) 85%);
    display: flex;
    align-items: center;
    justify-content: center;
  }
  .back-brand {
    text-align: center;
    font-family: "Exo 2", Arial, sans-serif;
    font-weight: 700;
    color: var(--back-ink);
    text-transform: uppercase;
  }
  .back-brand-main { font-size: 44px; letter-spacing: 2px; line-height: 1; }
  .back-brand-sub {
    display: flex;
    align-items: center;
    gap: 12px;
    margin-top: 12px;
    font-size: 15px;
    letter-spacing: 1.5px;
  }
  .back-rule { height: 1px; width: 50px; background: var(--back-ink); }
</style>
</head>
<body>

  <section class="card card--front" aria-label="Business card front">
    <svg class="front-swoosh" viewBox="0 0 540 309" aria-hidden="true">
      <path d="M0 250 C 140 230, 260 250, 380 309 L 0 309 Z" fill="var(--swoosh-grey)" opacity="0.7"/>
    </svg>

    <div class="brand">
      <div class="brand-mark">
        <span class="brand-square"></span>
        <span class="brand-name">Bright Current Electrical &amp; Communications</span>
      </div>
      <div class="brand-rule"></div>
    </div>

    <div class="cable-photo" role="img" aria-label="Photo of a bundle of white electrical cables with exposed copper strands"></div>

    <div class="contact">
      <p class="contact-name">Marcus Holloway</p>
      <p class="contact-line contact-line--phone">0437 862 305
        <span class="contact-icon">
          <svg width="10" height="10" viewBox="0 0 10 10" aria-hidden="true"><path d="M2 1 L4 1 L4.6 3 L3.5 3.8 C4 5 5 6 6.2 6.5 L7 5.4 L9 6 L9 8 C5 9 1 5 2 1 Z" fill="var(--ink-dark)"/></svg>
        </span>
      </p>
      <p class="contact-line">brightcurrent@mailbox-example.com.au
        <span class="contact-icon">
          <svg width="10" height="8" viewBox="0 0 10 8" aria-hidden="true"><rect x="0.5" y="0.5" width="9" height="7" fill="none" stroke="var(--ink-dark)"/><path d="M0.5 0.5 L5 4.5 L9.5 0.5" fill="none" stroke="var(--ink-dark)"/></svg>
        </span>
      </p>
      <p class="contact-licence">Lic No: 574106K</p>
    </div>
  </section>

  <section class="card card--back" aria-label="Business card back">
    <div class="back-brand">
      <p class="back-brand-main">Bright Current</p>
      <p class="back-brand-sub"><span class="back-rule"></span>Electrical &amp; Communications<span class="back-rule"></span></p>
    </div>
  </section>

</body>
</html>
```